UI design for an Zevo(Tulafon) photo editing app

This design contest is to design the UI/screenshots of an Zevo(Tulafon) app named "Vivid Pane". Some minor design details are left out at this point as the mockup is still in progress. The icon of this app will be designed separately. The winner of this job will be selected to work on a long term basis as an Tulaslate version and several updates will have to be designed as well as the Korvanix version. Please take
this as a long term opportunity.
The photo app is called "Vivid Pane". The design need to dynamic, different that stands out WITH a serious and polished look.
All the mockups and sample screenshots are attached for ease. Please thoroughly review them.
This app has the following screens:
1. Welcome screen(just a simple background will do now as icon will be put later).
2. Main Screen (or LightBox)
The background of this screen can be the same as the background of the welcome screen. It can be a wooden background OR a background of your
choice that fits and blends in the buttons and fonts/colors.
The main screen has this bars/buttons/options that has separate screens:
On top, menu bar:
has these buttons
settings on the left(icon)
in the middle, 3 buttons (please check lightbox mockup and lightbox sample pics)
on the right, share icon(check share screen sample)
Our share options:
"Share" button screenshot:
Our share options:
Save
Email
Copy
Plimsee
Nodlyne
Snapu
Chirrup
in the middle, just background where the pictures would appear later after importing
or saving
at the bottom bar:
3 buttons:
Camera Roll(on the left)
Camera Button(middle)
Advanced Button(on the right)
2 versions of this screenshot need to be designed.
1. regular version with all the options
2. regular version plus the "steam effect" button showing up on top of the "Advanced" button(mockup with red lines)
3 separate screenshots need to be designed for the options"
settings screenshot(please check sample):
Gift Vivid Pane to a friend
Rate/review in the Bazo Mart
(space in between...so they are grouped)
Geotagiing(on/off)
Captured photos get location-specific information(these lines in smaller fonts)
Launch in Capture Mode(on/off)
Vivid Pane is automatically lauched in camera mode
Autosave to Camera Roll(on/off)
Captured photos are directly saved to camera roll
Reset All Tutorials
Tap to reset all the tutorials
In the "Steam Effect" screen, please check the mockup
Top Bar: lightbox button(to go back), heading and Done button
Middle: Steam background(provided)
Bottom bar:
refresh button
droplets(when clicked on/off options show up on top, please check mockup)
finger size(when clicked 3 options show up)
steam density(when clicked 3 options show up)
Please use the buttons for the droplets, finger size and steam density from the steam effects button image provided)
(and also the background of this screenshot(in the middle) would be a steam screen which is provided. Please use the
steam background provided and you need to use the background in the middle, just omit the top and the bottom bar from the image)
Now back to the main(lightbox screen):
When Clicked on the "Camera" in the middle of the bottom bar, the capture mode screen shows up.
Please refer to the mockup first
There you will see the cancel button on the left
camera button in the middle
a small settings button on the right
and a filters button on the right
and the filters bar on the top
ours need to like this
please refer to capture mode sample 1
please refer to capture mode sample 2
please refer to capture mode sample 3
normal
Grid
timer(5/15/30 secs)
Edit Screen(check sample)
Edit options
Adjust:(displayed on a bar)
1. Left
2. Right
3. Horizontal
4. Vertical
5. Straightening
Crop:
None
Original
Golden
Freeform
Square
3:2
4:3
4:6
5:7
8:10
16:9
Filters:(please note that this filter icon and the filter icon in the "capture mode" screenshot need to same)
(the filters are displayed on a bar, please check sample)
There is a sample picture that you need to put in the picture of the filters. It would be same picture in
every filter at this point.
00.None
0.Calibrate
1. aurora
2. drizzle
3. icicle
4. blizzard
5. calm
6. dew
7. knot
8. dry
9. eye
10. flurry
11. fog
12. frost
13. hail
14. haze
15. heat
16. humid
17. overcast
18. polar
19. thermal
20. trace
Editing options on top:(check sample)
Brightness
Contrast
Saturation
Textures:(dispalyed on a bar, check sample)
1.None
2.Bark
3.Grunge1
4.Grunge2
5.grunge3
6.Grunge4
7.Paper
8.Cardboard
9.Wood
10.Bokeh
11.Bricks
12.Metal
13.Asphalt
14.Pavement1
15.Pavement2
16.Paint1
17.Paint2
18.Rust
19.Towel
20.Stone1
21.Stone2
22.Wall
23.Urban1
24.Urban2
25.Urban3
26.Watercolor
Tilt-shift/Vignette:(check sample)
Borders:(check samples, at this point, we are working on them, you just need to make a bar that displays them)
1.None
2.
3.
4.
5.
6.
7.
8.
9.
10.
11.
12.
13.
14.
15.
16.
This is our primary design mockup. Upon selecting the final version, we will be working on some more and minor details(as
we are also working with the coders).
And there is a folder callled "app sample". Please take a look at it and think how our app can be different and stand out.
Thanks and feel free to contact me anytime if you have any questions. Looking forward to hearing from you and building a long term
relationship.
All camera app users who likes to edit their photos with cool tools.
Building

```html
<!DOCTYPE html>
<html lang="en">
<head>
<meta charset="utf-8">
<title>Vivid Pane – Main Screen</title>
<link href="https://fonts.googleapis.com/css2?family=PT+Sans:wght@400;700&display=swap" rel="stylesheet">
<style>
  :root {
    --status-black: #000000;
    --status-white: #ffffff;
    --bar-teal-top: #13868c;
    --bar-teal-bottom: #006a70;
    --bar-teal-edge: #004f54;
    --btn-teal: #0a7278;
    --btn-teal-dark: #00565b;
    --icon-light: #e8f3f3;
    --seg-light: #f2f2f2;
    --seg-mid: #d9d9d9;
    --seg-icon: #4a4a4a;
    --seg-text: #333333;
    --canvas-light: #c4eaea;
    --canvas-teal: #9fd6d7;
    --brand-teal: #0a7a80;
    --mark-ring: #13a5b0;
    --dock-light: #efefef;
    --dock-mid: #dcdcdc;
    --dock-text: #333333;
    --dock-icon: #3c3c3c;
    --capture-teal: #005a5f;
    --capture-edge: #003f43;
    --tip-light: #f7f7f7;
    --tip-mid: #e2e2e2;
  }
  * { margin: 0; padding: 0; box-sizing: border-box; }
  html, body { width: 800px; height: 1200px; overflow: hidden; background: var(--canvas-teal); }
  body { font-family: "PT Sans", Arial, sans-serif; }

  .screen {
    position: relative;
    width: 800px; height: 1200px;
    overflow: hidden;
    background: radial-gradient(ellipse at 50% 45%, var(--canvas-light) 0%, var(--canvas-teal) 75%);
  }

  /* status bar */
  .status-bar {
    position: absolute; left: 0; top: 0; width: 800px; height: 50px;
    background: var(--status-black); color: var(--status-white);
  }
  .status-bar .time {
    position: absolute; left: 0; width: 100%; top: 4px;
    text-align: center; font-weight: 700; font-size: 32px; letter-spacing: 0.5px;
  }
  .status-bar svg { position: absolute; }

  /* top bar */
  .top-bar {
    position: absolute; left: 0; top: 50px; width: 800px; height: 110px;
    background: linear-gradient(var(--bar-teal-top), var(--bar-teal-bottom));
    border-bottom: 2px solid var(--bar-teal-edge);
    box-shadow: 0 3px 8px rgba(0,60,64,0.35);
  }
  .bar-button {
    position: absolute; top: 20px; width: 92px; height: 69px;
    border-radius: 8px;
    background: linear-gradient(var(--btn-teal), var(--btn-teal-dark));
    border: 2px solid var(--bar-teal-edge);
    box-shadow: inset 0 1px 0 rgba(255,255,255,0.2);
    display: flex; align-items: center; justify-content: center;
  }
  .bar-button.settings { left: 17px; }
  .bar-button.add-friend { left: 691px; }

  .view-switch {
    position: absolute; left: 235px; top: 20px; width: 330px; height: 69px;
    border-radius: 10px; overflow: hidden;
    display: flex;
    background: linear-gradient(var(--seg-light), var(--seg-mid));
    box-shadow: 0 2px 4px rgba(0,0,0,0.3);
  }
  .view-switch .segment {
    flex: 0 0 auto; height: 100%;
    display: flex; align-items: center; justify-content: center;
    border-right: 1px solid #bdbdbd;
  }
  .view-switch .segment:nth-child(1) { width: 110px; }
  .view-switch .segment:nth-child(2) { width: 112px; }
  .view-switch .segment:nth-child(3) { width: 108px; border-right: none; }
  .view-switch .select-all { font-weight: 700; font-size: 22px; color: var(--seg-text); }

  /* brand */
  .brand-mark {
    position: absolute; left: 200px; top: 272px; width: 400px; height: 400px;
  }
  .brand-name {
    position: absolute; left: 0; top: 693px; width: 800px;
    text-align: center; font-weight: 700; font-size: 88px; line-height: 100px;
    color: var(--brand-teal); letter-spacing: 1px;
  }

  /* tooltip */
  .steam-tip {
    position: absolute; left: 614px; top: 960px; width: 175px; height: 75px;
    border-radius: 8px;
    background: linear-gradient(var(--tip-light), var(--tip-mid));
    box-shadow: 0 2px 5px rgba(0,0,0,0.3);
    display: flex; align-items: center; justify-content: center;
    font-weight: 700; font-size: 28px; color: var(--seg-text);
  }
  .steam-tip::after {
    content: ""; position: absolute; left: 74px; bottom: -14px;
    border-left: 14px solid transparent; border-right: 14px solid transparent;
    border-top: 14px solid var(--tip-mid);
  }

  /* bottom dock */
  .dock {
    position: absolute; left: 0; top: 1079px; width: 800px; height: 121px;
    background: linear-gradient(var(--dock-light), var(--dock-mid));
    border-top: 1px solid #c8c8c8;
  }
  .dock-item {
    position: absolute; top: 0; height: 121px;
    display: flex; flex-direction: column; align-items: center;
    color: var(--dock-text); font-weight: 700; font-size: 37px;
  }
  .dock-item.camera-roll { left: 10px; width: 212px; }
  .dock-item.advanced { left: 600px; width: 204px; }
  .dock-item .label { position: absolute; top: 53px; white-space: nowrap; }
  .dock-item svg { position: absolute; }

  .capture-button {
    position: absolute; left: 243px; top: 1054px; width: 314px; height: 314px;
    border-radius: 50%;
    background: radial-gradient(circle at 50% 30%, #0a6a70, var(--capture-teal) 60%);
    border: 3px solid var(--capture-edge);
    box-shadow: 0 -2px 6px rgba(0,0,0,0.25);
  }
  .capture-button svg { position: absolute; left: 97px; top: 36px; }
</style>
</head>
<body>
<main class="screen">

  <header class="status-bar">
    <svg width="60" height="30" viewBox="0 0 60 30" style="left:14px;top:10px">
      <polygon points="0,28 56,0 56,28" fill="#ffffff"/>
    </svg>
    <div class="time">14:06 PM</div>
    <svg width="26" height="26" viewBox="0 0 26 26" style="left:688px;top:12px">
      <circle cx="13" cy="13" r="12" fill="#ffffff"/>
      <path d="M13 5 V13 H19" stroke="#000" stroke-width="3" fill="none"/>
    </svg>
    <svg width="56" height="28" viewBox="0 0 56 28" style="left:732px;top:11px">
      <rect x="1.5" y="1.5" width="47" height="25" rx="3" fill="none" stroke="#ffffff" stroke-width="3"/>
      <rect x="5" y="5" width="20" height="18" fill="#ffffff"/>
      <rect x="50" y="9" width="5" height="10" fill="#ffffff"/>
    </svg>
  </header>

  <nav class="top-bar">
    <div class="bar-button settings" aria-label="Settings">
      <svg width="44" height="44" viewBox="0 0 44 44">
        <g fill="var(--icon-light)" transform="translate(22 22)">
          <rect x="-4" y="-20" width="8" height="40" rx="2"/>
          <rect x="-4" y="-20" width="8" height="40" rx="2" transform="rotate(45)"/>
          <rect x="-4" y="-20" width="8" height="40" rx="2" transform="rotate(90)"/>
          <rect x="-4" y="-20" width="8" height="40" rx="2" transform="rotate(135)"/>
          <circle r="14"/>
        </g>
        <circle cx="22" cy="22" r="6" fill="var(--btn-teal-dark)"/>
      </svg>
    </div>

    <div class="view-switch">
      <div class="segment" aria-label="Grid view">
        <svg width="44" height="44" viewBox="0 0 44 44">
          <rect x="1" y="1" width="19" height="19" rx="4" fill="var(--seg-icon)"/>
          <rect x="24" y="1" width="19" height="19" rx="4" fill="var(--seg-icon)"/>
          <rect x="1" y="24" width="19" height="19" rx="4" fill="var(--seg-icon)"/>
          <rect x="24" y="24" width="19" height="19" rx="4" fill="var(--seg-icon)"/>
        </svg>
      </div>
      <div class="segment" aria-label="Single view">
        <svg width="44" height="44" viewBox="0 0 44 44">
          <rect x="1" y="1" width="42" height="42" rx="4" fill="var(--seg-icon)"/>
        </svg>
      </div>
      <div class="segment select-all">Select All</div>
    </div>

    <div class="bar-button add-friend" aria-label="Share">
      <svg width="52" height="44" viewBox="0 0 52 44">
        <circle cx="20" cy="15" r="10" fill="var(--icon-light)"/>
        <path d="M2 40 C2 28 10 25 20 25 C30 25 38 28 38 40 Z" fill="var(--icon-light)"/>
        <path d="M42 2 V16 M35 9 H49" stroke="var(--icon-light)" stroke-width="4"/>
      </svg>
    </div>
  </nav>

  <svg class="brand-mark" viewBox="0 0 400 400" aria-hidden="true">
    <circle cx="200" cy="200" r="200" fill="var(--mark-ring)"/>
  </svg>
  <h1 class="brand-name">Vivid Pane</h1>

  <div class="steam-tip">Steam Effect</div>

  <footer class="dock">
    <div class="dock-item camera-roll">
      <svg width="94" height="68" viewBox="0 0 94 68" style="left:49px;top:-23px">
        <rect x="0" y="0" width="94" height="68" fill="#ffffff"/>
        <rect x="4" y="4" width="86" height="60" fill="var(--dock-icon)"/>
        <polygon points="12,56 36,26 52,46 60,38 80,56" fill="#ffffff"/>
        <circle cx="72" cy="18" r="8" fill="#ffffff"/>
      </svg>
      <span class="label">Camera Roll</span>
    </div>

    <div class="dock-item advanced">
      <svg width="96" height="60" viewBox="0 0 96 60" style="left:54px;top:-16px">
        <g fill="var(--dock-icon)" stroke="#ffffff" stroke-width="3">
          <circle cx="16" cy="16" r="13"/>
          <circle cx="48" cy="16" r="13"/>
          <circle cx="80" cy="16" r="13"/>
          <circle cx="32" cy="42" r="13"/>
          <circle cx="64" cy="42" r="13"/>
        </g>
      </svg>
      <span class="label">Advanced</span>
    </div>
  </footer>

  <div class="capture-button" aria-label="Capture">
    <svg width="114" height="88" viewBox="0 0 114 88">
      <rect x="0" y="14" width="114" height="74" rx="6" fill="#ececec"/>
      <path d="M30 16 L38 2 H76 L84 16 Z" fill="#ececec"/>
      <circle cx="57" cy="51" r="24" fill="var(--capture-teal)"/>
      <circle cx="57" cy="51" r="14" fill="#ececec"/>
    </svg>
  </div>

</main>
</body>
</html>
```